Stand bag for exclusive, natural snacks

We are looking for a PP stand bag design that will be used to pack exclusive snacks (dried fruits). These snacks will be 100% natural, healthy and without any chemicals. For that reason and for the fact that these products will have a higher price point, the stand bag design should look very premium and happy, while still reminding the customer of the natural, healthy benefits of the snacks inside. The main colors of our brand are black and gold, so we would like to see the packaging in similar colors. In order to be able to see the product, we usually leave some part of the PP packaging transparent.
Packaging Size: h170mm x w80mm x d30mm

Target Market(s)

High-end retail markets with consumers that are willing to pay a little more to get a high-quality product, free from any preservatives and completely natural.

Font styles to use
Sans Serif

Colors

Designer to choose colors to be used in the design.

Requirements
Must have
• - similar to the bag in the sample photos
• - bag size: h170mm x w80mm x d30mm
• - Our logo
• - the colors black & gold
• - Some way of showing the customer the benefit of our dried fruits (healthy, natural, happy)
• - a transparent part to see the product through the plastic foil
Nice to have
• - bottom maybe not transparent in order not to see dust that falls to the bottom

```html
<!DOCTYPE html>
<html lang="en">
<head>
<meta charset="utf-8">
<title>Amber Larder – Dried Fruits Cranberry Stand Bag Front</title>
<link href="https://fonts.googleapis.com/css2?family=Crimson+Pro:wght@400;600;700&display=swap" rel="stylesheet">
<style>
  :root {
    --page-bg: #ffffff;
    --bag-black: #221f1f;
    --gold: #c6a862;
    --gold-deep: #8a7440;
    --ink: #1a1717;
    --white: #ffffff;
    --window-grey: #c8c9cb;
  }
  * { box-sizing: border-box; margin: 0; padding: 0; }
  html, body {
    width: 1200px;
    height: 960px;
    overflow: hidden;
    background: var(--page-bg);
  }
  .canvas {
    position: relative;
    width: 1200px;
    height: 960px;
  }
  .bag-front {
    position: absolute;
    left: 400px;
    top: 55px;
    width: 400px;
    height: 850px;
    background: var(--bag-black);
    overflow: hidden;
    font-family: "Crimson Pro", "Times New Roman", serif;
  }
  .brand-ribbon {
    position: absolute;
    left: 155px;
    top: 0;
    width: 90px;
    height: 227px;
  }
  .brand-name {
    position: absolute;
    left: 100px;
    top: 112px;
    width: 200px;
    text-align: center;
    color: var(--ink);
    font-weight: 600;
    font-size: 19px;
    line-height: 1.05;
    letter-spacing: 0.12em;
    text-transform: uppercase;
  }
  .fruit-sketch {
    position: absolute;
    background: linear-gradient(160deg, rgba(198,168,98,0.28), rgba(138,116,64,0.12) 70%, rgba(34,31,31,0));
  }
  .fruit-sketch--left {
    left: 0;
    top: 218px;
    width: 96px;
    height: 293px;
    border-radius: 0 60px 40px 0;
  }
  .fruit-sketch--right {
    right: 0;
    top: 211px;
    width: 93px;
    height: 300px;
    border-radius: 60px 0 0 40px;
  }
  .product-title {
    position: absolute;
    left: 0;
    top: 248px;
    width: 100%;
    text-align: center;
    color: var(--white);
    font-weight: 400;
    font-size: 67px;
    line-height: 0.86;
    letter-spacing: 0.01em;
  }
  .product-window {
    position: absolute;
    left: 92px;
    top: 390px;
    width: 216px;
    height: 272px;
    background: var(--window-grey);
    border-radius: 32px;
  }
  .flavour-band {
    position: absolute;
    left: 0;
    top: 513px;
    width: 100%;
    height: 71px;
    background: var(--gold);
    text-align: center;
    color: var(--ink);
  }
  .flavour-name {
    display: block;
    margin-top: 6px;
    font-weight: 700;
    font-size: 40px;
    line-height: 1;
    letter-spacing: 0.06em;
  }
  .flavour-claim {
    display: block;
    margin-top: 3px;
    font-weight: 700;
    font-size: 14px;
    letter-spacing: 0.1em;
  }
  .net-weight {
    position: absolute;
    left: 0;
    top: 678px;
    width: 100%;
    text-align: center;
    color: var(--white);
    font-weight: 700;
    font-size: 21px;
    letter-spacing: 0.04em;
  }
</style>
</head>
<body>
  <main class="canvas">
    <section class="bag-front">
      <svg class="brand-ribbon" viewBox="0 0 90 227" aria-hidden="true">
        <polygon points="0,0 90,0 90,227 45,216 0,227" fill="var(--gold)"/>
      </svg>
      <p class="brand-name">Amber<br>Larder</p>

      <div class="fruit-sketch fruit-sketch--left" role="img" aria-label="Gold line sketch of apricot, plum and papaya halves"></div>
      <div class="fruit-sketch fruit-sketch--right" role="img" aria-label="Gold line sketch of berries, grapes and strawberries"></div>

      <h1 class="product-title">DRIED<br>FRUITS</h1>

      <div class="product-window" role="img" aria-label="Transparent window showing the dried cranberries inside"></div>

      <div class="flavour-band">
        <span class="flavour-name">CRANBERRY</span>
        <span class="flavour-claim">100% NATURAL SNACK</span>
      </div>

      <p class="net-weight">125 G</p>
    </section>
  </main>
</body>
</html>
```